Prepare a modern, professional business card for Meridel Vantage Advisory (MVA) Our company is in the banking, compliance and finance industry. We provide kiosks, software integration, and compliance guidelines so that banks can "bank" Marijuana Dispensaries with MonLex, Office of Statute Review and NBRA approval.

Target Market(s)

Banks

Industry/Entity Type

Business

Contact Information for Business Card

Peter L Oakridge
Meridel Vantage Advisory
Vice President
4427 Larkspur Crossing Way
Suite 218
Brennfield, OR 97381
pete@mvalq.com
555-418-7362

Font styles to use
Sans Serif

Requirements
Nice to have
• I like the clean simple appearance of Quince computers. Perhaps the three LETTERS of MVA can be the LOGO on the Card and the Company name could be incorporated in the contact information. Like colors of white, black and gray

```html
<!DOCTYPE html>
<html lang="en">
<head>
<meta charset="utf-8">
<title>Meridel Vantage Advisory – Business Card</title>
<link rel="stylesheet" href="https://fonts.googleapis.com/css2?family=Source+Sans+3:wght@400;600;700&display=swap">
<style>
  :root {
    --backdrop: #2f3d45;
    --card-dark: #595959;
    --card-light: #ffffff;
    --ink: #1e1e1e;
    --ink-muted: #7a7a7a;
    --mark-gray: #6e6e6e;
    --on-dark: #ffffff;
    --accent-blue: #6cc6e3;
  }
  html, body {
    margin: 0;
    width: 1200px;
    height: 1000px;
    overflow: hidden;
    background: var(--backdrop);
    font-family: "Source Sans 3", "Myriad Pro", Arial, sans-serif;
  }
  .canvas {
    position: relative;
    width: 1200px;
    height: 1000px;
  }
  .card {
    position: absolute;
    left: 270px;
    width: 660px;
    height: 378px;
    border-radius: 4px;
    box-sizing: border-box;
    box-shadow: 0 10px 28px rgba(0,0,0,0.35);
  }
  .card-back {
    top: 60px;
    background: var(--card-dark);
    display: flex;
    flex-direction: column;
    align-items: center;
    justify-content: center;
    gap: 26px;
  }
  .card-back .wordmark {
    color: var(--on-dark);
    font-weight: 700;
    font-size: 96px;
    line-height: 1;
    letter-spacing: 2px;
  }
  .card-back .slogan {
    color: var(--on-dark);
    font-weight: 600;
    font-size: 24px;
    margin: 0;
  }
  .card-back .slogan .highlight {
    color: var(--accent-blue);
  }
  .card-front {
    top: 520px;
    background: var(--card-light);
  }
  .card-front .wordmark {
    position: absolute;
    left: 42px;
    top: 150px;
    color: var(--mark-gray);
    font-weight: 700;
    font-size: 82px;
    line-height: 1;
    letter-spacing: 1px;
  }
  .contact {
    position: absolute;
    left: 288px;
    top: 48px;
    color: var(--ink);
    font-size: 20px;
    line-height: 1.42;
    white-space: nowrap;
  }
  .contact p { margin: 0; }
  .person-name { font-weight: 700; font-size: 22px; }
  .person-title { color: var(--ink-muted); margin-bottom: 38px !important; }
  .company-name { font-weight: 700; }
  .address { margin-bottom: 16px !important; }
  .phone .label { margin-right: 12px; }
  .web .domain { font-weight: 700; }
</style>
</head>
<body>
<main class="canvas">
  <section class="card card-back" aria-label="Card back">
    <div class="wordmark">MVA</div>
    <p class="slogan">Can Put Slogan Here <span class="highlight">Would Be Nice</span></p>
  </section>

  <section class="card card-front" aria-label="Card front">
    <div class="wordmark">MVA</div>
    <div class="contact">
      <p class="person-name">Peter L Oakridge</p>
      <p class="person-title">Vice President</p>
      <p class="company-name">Meridel Vantage Advisory</p>
      <p class="address">4427 Larkspur Crossing Way, Suite 218<br>Brennfield, OR 97381</p>
      <p class="phone"><span class="label">T</span>555-418-7362</p>
      <p class="email">peter.oakridge@mvalq.com</p>
      <p class="web">www.<span class="domain">mvalq</span>.com</p>
    </div>
  </section>
</main>
</body>
</html>
```